Unique Elegant Stationary Set

Prepare a unique eye catching stationary set consisting of :
(1) Letterhead
(2) A3 Envelope
(3) Business Card
(4) Email Signature Banner

Package to be elegant, modern, and designers not only to think of design or colors but also materials could make a big difference, embossing, debossing, glossy, matt ....etc.

I attached both our new logos (Stacked or Linear) noting you may use any of them but you cant modify anything in the logos. Also attached our final draft portfolio to see what type of projects we work on and i also have here a glimboard page link showing the direction we want: https://www.glimboard.example/ravelkoton/business-card-design/

Target Market(s)

VVIP / Elite Developers

Industry/Entity Type

Architecture

Font styles to use
Sans Serif
Other font styles liked:
• unitext

Requirements
Should not have
• too many colors, or being busy in general. We want something pleasing to the eye

```html
<!DOCTYPE html>
<html lang="en">
<head>
<meta charset="utf-8">
<title>Vantor Studio — Stationery Set</title>
<link href="https://fonts.googleapis.com/css2?family=Montserrat:wght@400;500;600&display=swap" rel="stylesheet">
<style>
  :root{
    --board:#e7e8ea;
    --paper:#ffffff;
    --shadow:#4e4c4a;
    --ink:#1b1b1b;
    --ink-soft:#3a3a3a;
    --accent:#d32027;
    --mark:#e2e2e2;
    --rule:#9a9a9a;
  }
  *{margin:0;padding:0;box-sizing:border-box}
  html,body{width:1200px;height:1163px;overflow:hidden}
  body{background:var(--board);font-family:"Montserrat",sans-serif;color:var(--ink);position:relative}

  .section-title{position:absolute;font-weight:600;font-size:24px;transform:translateX(-50%);white-space:nowrap;letter-spacing:.2px}

  .sheet{position:absolute;background:var(--paper);filter:drop-shadow(-19px 17px 5px var(--shadow))}

  .brand{position:absolute;color:var(--mark);font-weight:500;text-align:center;line-height:1;transform:translateX(-50%);white-space:nowrap}
  .brand-name{display:block;letter-spacing:.08em}
  .brand-sub{display:block;letter-spacing:.9em;margin-right:-.9em}

  .contact-row{position:absolute;display:flex;align-items:center;font-size:9.4px;color:var(--ink);white-space:nowrap;transform:translateX(-50%)}
  .contact-row .item{display:flex;align-items:center;gap:8px}
  .contact-row .sep{width:1px;height:11px;background:var(--rule);margin:0 8px}
  .icon{width:9px;height:9px;fill:var(--accent);flex:none}

  .person{position:absolute}
  .person .name{font-weight:600;color:var(--ink)}
  .person .name .first{color:var(--accent)}
  .person .role{color:var(--ink-soft)}
  .person ul{list-style:none}
  .person li{display:flex;align-items:center;color:var(--ink-soft)}

  /* letterhead */
  .letterhead{left:78px;top:83px;width:482px;height:682px}
  /* cards */
  .card{top:83px;width:166px;height:290px}
  .card-front{left:729px}
  .card-back{left:952px}
  .card .person{left:21px;top:226px}
  .card .name{font-size:7.4px}
  .card .role{font-size:4.6px;margin-top:1px}
  .card ul{margin-top:6px}
  .card li{font-size:4.8px;gap:5px;height:7px}
  .card .icon{width:5px;height:5px}
  /* envelope */
  .envelope{position:absolute;left:689px;top:487px;width:413px;height:579px;filter:drop-shadow(-19px 17px 5px var(--shadow))}
  .envelope svg.shape{position:absolute;inset:0}
  .envelope .contact-row{font-size:7.8px}
  .envelope .contact-row .item{gap:6px}
  .envelope .contact-row .sep{height:10px;margin:0 6px}
  .envelope .contact-row .icon{width:8px;height:8px}
  /* email banner */
  .banner{left:78px;top:873px;width:482px;height:194px}
  .banner .divider{position:absolute;left:319px;top:71px;width:1px;height:53px;background:var(--rule)}
  .banner .person{left:327px;top:70px}
  .banner .name{font-size:9.4px}
  .banner .role{font-size:6.4px;margin-top:1px}
  .banner ul{margin-top:5px}
  .banner li{font-size:6.8px;gap:7px;height:11.5px}
  .banner .icon{width:6.5px;height:6.5px}
</style>
</head>
<body>

<svg width="0" height="0" style="position:absolute" aria-hidden="true">
  <defs>
    <symbol id="i-phone" viewBox="0 0 24 24"><path d="M6.6 10.8a15.2 15.2 0 0 0 6.6 6.6l2.2-2.2c.3-.3.7-.4 1-.2 1.1.4 2.3.6 3.6.6.6 0 1 .4 1 1V20c0 .6-.4 1-1 1A17 17 0 0 1 3 4c0-.6.4-1 1-1h3.5c.6 0 1 .4 1 1 0 1.3.2 2.5.6 3.6.1.3 0 .7-.2 1z"/></symbol>
    <symbol id="i-mail" viewBox="0 0 24 24"><path d="M2 5h20v14H2z M3.5 6.5 12 13l8.5-6.5" fill-rule="evenodd"/><path d="M3 6l9 7 9-7" stroke="#fff" stroke-width="1.6" fill="none"/></symbol>
    <symbol id="i-globe" viewBox="0 0 24 24"><circle cx="12" cy="12" r="10"/><path d="M2 12h20M12 2c3 3 3 17 0 20M12 2c-3 3-3 17 0 20M4 7h16M4 17h16" stroke="#fff" stroke-width="1.3" fill="none"/></symbol>
  </defs>
</svg>

<!-- Letterhead -->
<h2 class="section-title" style="left:318px;top:37px">Letterhead</h2>
<section class="sheet letterhead">
  <div class="brand" style="left:241px;top:40px">
    <span class="brand-name" style="font-size:46px">VANTOR</span>
    <span class="brand-sub" style="font-size:17px;margin-top:10px">STUDIO</span>
  </div>
  <div class="contact-row" style="left:241px;top:632px">
    <span class="item"><svg class="icon"><use href="#i-phone"/></svg>+00 555 014782</span><span class="sep"></span>
    <span class="item"><svg class="icon"><use href="#i-mail"/></svg>contact@vantorstudio.example</span><span class="sep"></span>
    <span class="item"><svg class="icon"><use href="#i-globe"/></svg>www.vantorstudio.example</span>
  </div>
</section>

<!-- Business cards -->
<h2 class="section-title" style="left:922px;top:37px">Business Card</h2>
<section class="sheet card card-front">
  <div class="brand" style="left:70px;top:170px">
    <span class="brand-name" style="font-size:22px">VANTOR</span>
    <span class="brand-sub" style="font-size:8px;margin-top:6px">STUDIO</span>
  </div>
  <div class="person">
    <div class="name"><span class="first">Elias</span> Marlow</div>
    <div class="role">Principle Architecture</div>
    <ul>
      <li><svg class="icon"><use href="#i-phone"/></svg>+00 555 014782</li>
      <li><svg class="icon"><use href="#i-mail"/></svg>contact@vantorstudio.example</li>
      <li><svg class="icon"><use href="#i-globe"/></svg>www.vantorstudio.example</li>
    </ul>
  </div>
</section>
<section class="sheet card card-back">
  <div class="brand" style="left:85px;top:137px">
    <span class="brand-name" style="font-size:27px">VANTOR</span>
    <span class="brand-sub" style="font-size:9.5px;margin-top:8px">STUDIO</span>
  </div>
</section>

<!-- A3 envelope -->
<h2 class="section-title" style="left:900px;top:439px">A3 Envelope</h2>
<section class="envelope">
  <svg class="shape" width="413" height="579" viewBox="0 0 413 579" aria-hidden="true">
    <path d="M0 93 L24 14 Q28 0 44 0 L369 0 Q385 0 389 14 L413 93 L413 579 L0 579 Z" fill="#fff"/>
    <line x1="0" y1="93" x2="413" y2="93" stroke="#ececec" stroke-width="1.2"/>
  </svg>
  <div class="brand" style="left:206px;top:26px">
    <span class="brand-name" style="font-size:23px">VANTOR</span>
    <span class="brand-sub" style="font-size:8.5px;margin-top:6px">STUDIO</span>
  </div>
  <div class="brand" style="left:206px;top:240px">
    <span class="brand-name" style="font-size:56px">VANTOR</span>
    <span class="brand-sub" style="font-size:19px;margin-top:14px">STUDIO</span>
  </div>
  <div class="contact-row" style="left:206px;top:546px">
    <span class="item"><svg class="icon"><use href="#i-phone"/></svg>+00 555 014782</span><span class="sep"></span>
    <span class="item"><svg class="icon"><use href="#i-mail"/></svg>contact@vantorstudio.example</span><span class="sep"></span>
    <span class="item"><svg class="icon"><use href="#i-globe"/></svg>www.vantorstudio.example</span>
  </div>
</section>

<!-- Email signature banner -->
<h2 class="section-title" style="left:318px;top:820px">Email Signature Banner</h2>
<section class="sheet banner">
  <div class="brand" style="left:89px;top:73px">
    <span class="brand-name" style="font-size:27px">VANTOR</span>
    <span class="brand-sub" style="font-size:9.5px;margin-top:8px">STUDIO</span>
  </div>
  <span class="divider"></span>
  <div class="person">
    <div class="name"><span class="first">Elias</span> Marlow</div>
    <div class="role">Principle Architecture</div>
    <ul>
      <li><svg class="icon"><use href="#i-phone"/></svg>+00 555 014782</li>
      <li><svg class="icon"><use href="#i-mail"/></svg>contact@vantorstudio.example</li>
      <li><svg class="icon"><use href="#i-globe"/></svg>www.vantorstudio.example</li>
    </ul>
  </div>
</section>

</body>
</html>
```